Intuitive, look stunning website design for the street-level digital media platform that connects audiences with dynamic media on taxis and rideshare vehicles on BACK AND SIDE WINDOWS OF THE VEHICLE. SO FOOT TRAFFIC AND ALL OTHER TRAFFIC CAN SEE DISPLAY ON MOVING VEHICLE (in the future high glass building glass concept)
There should be 7 tabs VORTELANE as home button, advertisers, partners, drivers, about us, news and contact.

Target Market(s)

The company works with taxi companies and rideshare drivers to install its proprietary advertising displays in their vehicles. These proprietary screens deliver dynamic content based on location-based, WiFi-enabled triggers.

Vortelane provides an additional revenue stream to maximize drive time and empowers brands to efficiently engage consumers across our nation's busiest cities, including San Francisco, Los Angeles, New York City, Dallas, Austin, Chicago and Miami.

Industry/Entity Type

Digital Marketing

Coding

Coded - Design and coding required

Number of Pages Required

5+ page

Font styles to use
Sans Serif

Requirements
Must have
• Use beautiful graphics and easy to read fonts.
Make sure graphics are compressed and optimized for fast loading.
Design should be consistent on brand throughout the website design.
Design an intuitive navigation system which allows users to get to the pages they need quickly.
Create pages that are standard for all business from small to big such; home, about us, product/services , sitemap ( seo purposes) contact us etc..
icons links for snapchat, instagram, client login, facbook
Nice to have
• Out of box concept
Should not have
• ITS NOT AN LCD BOX PLACED OVER THE CAR

```html
<!DOCTYPE html>
<html lang="en">
<head>
<meta charset="utf-8">
<title>Vortelane — Street-Level Digital Media</title>
<link href="https://fonts.googleapis.com/css2?family=Bebas+Neue&family=Poppins:wght@400;500;600;700&display=swap" rel="stylesheet">
<style>
:root{
  --blue:#1d8fd0;
  --blue-dark:#0c4f8c;
  --footer:#2388c9;
  --ink:#111417;
  --text:#3d4248;
  --muted:#6b7178;
  --line:#e3e6ea;
  --white:#ffffff;
}
*{box-sizing:border-box;margin:0;padding:0}
html,body{width:1200px;height:3581px;overflow:hidden}
body{position:relative;background:var(--white);font-family:'Poppins',sans-serif;color:var(--text)}
.abs{position:absolute}
.display{font-family:'Bebas Neue',sans-serif;font-weight:400;color:var(--ink);letter-spacing:.5px}

/* header */
.logo{left:89px;top:44px;font-family:'Bebas Neue',sans-serif;font-size:50px;line-height:1;color:var(--ink);letter-spacing:.5px}
.contact-item{top:24px;display:flex;gap:10px;font-size:12px;line-height:17px;color:var(--ink)}
.contact-item b{display:block;font-weight:600;font-size:11px}
.contact-sep{left:757px;top:22px;width:1px;height:40px;background:var(--line)}
.login-btn{left:972px;top:24px;width:139px;height:37px;background:var(--blue-dark);color:var(--white);font-size:12px;font-weight:600;display:flex;align-items:center;justify-content:center}
.navbar{left:362px;top:88px;width:838px;height:48px;background:var(--blue);clip-path:polygon(32px 0,100% 0,100% 100%,0 100%)}
.header-rule{left:0;top:134px;width:370px;height:3px;background:var(--blue)}
.nav{top:104px;font-size:13px;font-weight:500;color:var(--white);letter-spacing:.3px}
.nav-sep{top:102px;width:1px;height:18px;background:rgba(255,255,255,.45)}

/* hero */
.hero{left:0;top:137px;width:1200px;height:628px;background:linear-gradient(110deg,#1a1a1d 0%,#3a3330 30%,#b77516 52%,#d99a2b 62%,#4a4138 78%,#1c1c1f 100%)}
.hero-shade{left:0;top:137px;width:1200px;height:628px;background:linear-gradient(180deg,rgba(0,0,0,.15),rgba(0,0,0,.45))}
.hero-kicker{left:97px;top:322px;font-size:36px;color:var(--white)}
.hero-title{left:88px;top:352px;font-size:118px;line-height:1;color:var(--white)}
.hero-lead{left:89px;top:468px;font-size:15px;color:var(--white)}
.hero-btn{left:90px;top:512px;width:138px;height:40px;background:var(--white);color:var(--ink);font-size:12px;font-weight:600;display:flex;align-items:center;justify-content:center}
.slide-count{left:1140px;font-size:22px;font-weight:600;color:var(--white)}
.slide-bar{left:1154px;top:402px;width:3px;height:56px;background:var(--white)}
.scroll-down{left:587px;top:694px;width:44px;height:44px;border-radius:50%;background:rgba(70,70,70,.85)}

/* about */
.about-visual{left:125px;top:841px;width:487px;height:431px;background:radial-gradient(ellipse at 50% 55%,#2f5fc9 0%,#1f46a3 45%,#e9edf4 75%,#ffffff 100%)}
.about-kicker{left:666px;top:873px;font-size:16px;font-weight:500;color:var(--ink)}
.about-title{left:666px;top:895px;font-size:60px;line-height:1}
.about-rule{left:633px;top:958px;width:70px;height:3px;background:var(--ink)}
.about-text{left:666px;width:400px;font-size:14px;line-height:20.5px;color:var(--text)}
.btn-dark{background:var(--blue-dark);color:var(--white);font-size:12px;font-weight:600;display:flex;align-items:center;justify-content:center}

/* services */
.section-title{left:0;width:1200px;text-align:center;font-size:60px;line-height:1}
.service-label{width:200px;text-align:center;font-size:14px;font-weight:600;line-height:22px;color:var(--ink);letter-spacing:.3px}

/* cta */
.cta{left:0;top:1745px;width:1200px;height:225px;background:linear-gradient(90deg,#1f86c7,#2a9ad8 60%,#1e89cb)}
.cta-title{left:83px;top:1818px;font-size:54px;line-height:1;color:var(--white)}
.cta-sub{left:83px;top:1874px;font-size:16px;font-weight:500;color:var(--white);letter-spacing:.6px}
.field{top:1850px;width:237px;height:28px;border-bottom:2px solid var(--white);font-size:13px;font-weight:600;color:var(--white)}
.send{left:988px;top:1835px;width:116px;height:44px;background:var(--white);color:var(--ink);font-size:17px;font-weight:700;display:flex;align-items:center;justify-content:center;letter-spacing:.5px}

/* stats */
.stat{width:440px;text-align:center}
.stat-num{font-family:'Poppins',sans-serif;font-size:64px;font-weight:700;color:var(--blue-dark);line-height:1}
.stat-label{font-size:22px;color:var(--muted);letter-spacing:.5px;margin-top:6px}
.divider{left:89px;top:2312px;width:1023px;height:1px;background:var(--line)}

/* blog */
.card{top:2468px;width:323px;height:403px;background:var(--white);box-shadow:0 6px 16px rgba(0,0,0,.12)}
.card-img{width:323px;height:200px}
.card-body{padding:22px 26px 0}
.card-date{font-size:11px;font-weight:600;color:var(--text);letter-spacing:.4px}
.card-title{margin-top:9px;font-size:14px;font-weight:700;line-height:18px;color:var(--ink);letter-spacing:.3px}
.card-text{margin-top:12px;font-size:13px;line-height:17px;color:var(--text)}
.card-link{display:inline-block;margin-top:11px;font-size:13px;font-weight:600;color:var(--blue);border-bottom:1px solid var(--blue);letter-spacing:.4px}

/* partners */
.partner{top:3042px;width:196px;height:78px;border:1px solid var(--line);display:flex;align-items:center;justify-content:center}
.partner span{display:block;width:86px;height:22px;border-radius:3px;background:#c9ced4}

/* footer */
.footer{left:0;top:3200px;width:1200px;height:381px;background:var(--footer)}
.footer-logo{left:89px;top:3331px;font-family:'Bebas Neue',sans-serif;font-size:52px;line-height:1;color:var(--white)}
.social{top:3392px;width:34px;height:34px;border-radius:50%;background:rgba(255,255,255,.18)}
.social i{position:absolute;left:12px;top:12px;width:10px;height:10px;border-radius:50%;background:var(--white)}
.fcol-title{top:3276px;font-family:'Bebas Neue',sans-serif;font-size:24px;color:var(--white);letter-spacing:.4px}
.fcol{top:3316px;font-size:13.5px;line-height:26.8px;color:var(--white)}
.fcontact{left:888px;font-size:13.5px;line-height:18px;color:var(--white);display:flex;gap:10px}
.footer-rule{left:89px;top:3517px;width:1023px;height:1px;background:rgba(255,255,255,.3)}
.copyright{left:0;top:3540px;width:1200px;text-align:center;font-size:13px;color:var(--white)}
.pay{top:3537px;width:44px;height:26px;border-radius:4px;background:var(--white)}
.to-top{left:1130px;top:3484px;width:40px;height:40px;border-radius:50%;background:var(--blue);border:1px solid rgba(255,255,255,.5)}
</style>
</head>
<body>

<!-- header -->
<div class="abs logo">VORTELANE</div>

<div class="abs contact-item" style="left:600px">
  <svg width="16" height="16" viewBox="0 0 24 24"><path d="M6.6 10.8a15 15 0 0 0 6.6 6.6l2.2-2.2c.3-.3.7-.4 1-.2 1.1.4 2.3.6 3.6.6.6 0 1 .4 1 1V20c0 .6-.4 1-1 1A17 17 0 0 1 3 4c0-.6.4-1 1-1h3.5c.6 0 1 .4 1 1 0 1.3.2 2.5.6 3.6.1.3 0 .7-.2 1z" fill="#1d8fd0"/></svg>
  <div><b>PHONE</b>+08 123 456 7890</div>
</div>
<div class="abs contact-sep"></div>
<div class="abs contact-item" style="left:785px">
  <svg width="18" height="16" viewBox="0 0 24 20"><rect x="1" y="2" width="22" height="16" rx="2" fill="#1d8fd0"/><path d="M2 4l10 7 10-7" stroke="#fff" stroke-width="2" fill="none"/></svg>
  <div><b>EMAIL</b>Info@example.com</div>
</div>
<div class="abs login-btn">CLIENT LOGIN</div>

<div class="abs navbar"></div>
<div class="abs header-rule"></div>
<div class="abs nav" style="left:427px">ADVERTISERS</div>
<div class="abs nav-sep" style="left:540px"></div>
<div class="abs nav" style="left:562px">PARTNERS</div>
<div class="abs nav-sep" style="left:652px"></div>
<div class="abs nav" style="left:675px">DRIVERS</div>
<div class="abs nav-sep" style="left:755px"></div>
<div class="abs nav" style="left:776px">ABOUT US</div>
<div class="abs nav-sep" style="left:866px"></div>
<div class="abs nav" style="left:888px">NEWS</div>
<div class="abs nav-sep" style="left:950px"></div>
<div class="abs nav" style="left:971px">CONTACT</div>
<svg class="abs" style="left:1059px;top:102px" width="20" height="20" viewBox="0 0 20 20"><circle cx="8" cy="8" r="6" stroke="#fff" stroke-width="2.4" fill="none"/><path d="M12.5 12.5l5 5" stroke="#fff" stroke-width="2.6" stroke-linecap="round"/></svg>

<!-- hero -->
<div class="abs hero" role="img" aria-label="Orange SUV parked in a dim garage, photographed from a low front angle"></div>
<div class="abs hero-shade"></div>
<div class="abs display hero-kicker">WELCOME TO VORTELANE</div>
<div class="abs display hero-title">ADVERTISING</div>
<div class="abs hero-lead">Lorem ipsum dolor sit amet consectetur adipisicing elit sed do....</div>
<div class="abs hero-btn">FIND OUT MORE</div>
<div class="abs slide-count" style="top:366px">02</div>
<div class="abs slide-bar"></div>
<div class="abs slide-count" style="top:464px">05</div>
<div class="abs scroll-down"></div>
<svg class="abs" style="left:603px;top:710px" width="12" height="12" viewBox="0 0 12 12"><path d="M2 4l4 4 4-4" stroke="#fff" stroke-width="2" fill="none"/></svg>

<!-- about -->
<div class="abs about-visual" role="img" aria-label="Rear view of a blue sedan on a white background"></div>
<div class="abs about-kicker">ABOUT US</div>
<div class="abs display about-title">WE ARE WORKING</div>
<div class="abs about-rule"></div>
<p class="abs about-text" style="top:985px">The company works with taxi companies and rideshare drivers to install its proprietary advertising displays in their vehicles. These proprietary screens deliver dynamic content based on location-based, WiFi-enabled triggers.</p>
<p class="abs about-text" style="top:1102px">Vortelane provides an additional revenue stream to maximize drive time and...</p>
<div class="abs btn-dark" style="left:666px;top:1168px;width:138px;height:41px">FIND OUT MORE</div>

<!-- services -->
<div class="abs display section-title" style="top:1326px">OUR BEST SERVICES</div>
<svg class="abs" style="left:0;top:1420px" width="1200" height="260" viewBox="0 1420 1200 260">
  <g fill="none" stroke="#bfc4c9" stroke-width="1.5" stroke-dasharray="5 5">
    <path d="M175 1536 A108 108 0 0 1 390 1546"/>
    <path d="M390 1546 A108 108 0 0 0 600 1546"/>
    <path d="M600 1546 A106 106 0 0 1 812 1546"/>
    <path d="M812 1546 A106 106 0 0 0 1024 1551"/>
  </g>
  <circle cx="175" cy="1536" r="9" fill="#c4c8cc"/>
  <circle cx="1024" cy="1551" r="9" fill="#c4c8cc"/>
  <g fill="#9aa0a6"><path d="M385 1544l5 7 5-7z"/><path d="M595 1552l5-7 5 7z"/><path d="M807 1544l5 7 5-7z"/></g>

  <!-- customizing your campaign -->
  <g transform="translate(246 1505)">
    <rect x="2" y="18" width="50" height="26" rx="6" fill="#1d8fd0"/>
    <path d="M10 18l6-12h22l6 12z" fill="#1d8fd0"/>
    <rect x="26" y="34" width="52" height="28" rx="6" fill="#0c4f8c"/>
    <path d="M34 34l7-14h22l7 14z" fill="#0c4f8c"/>
    <rect x="39" y="23" width="26" height="9" rx="2" fill="#fff"/>
    <circle cx="36" cy="48" r="4" fill="#fff"/><circle cx="68" cy="48" r="4" fill="#fff"/>
    <rect x="30" y="60" width="10" height="8" fill="#0c4f8c"/><rect x="64" y="60" width="10" height="8" fill="#0c4f8c"/>
    <rect x="22" y="6" width="56" height="24" rx="5" fill="#1d8fd0" opacity=".0"/>
  </g>
  <!-- launching and tracking -->
  <g transform="translate(448 1503)">
    <path d="M23 2a10 10 0 0 1 10 10c0 8-10 18-10 18S13 20 13 12A10 10 0 0 1 23 2z" fill="#0c4f8c"/>
    <circle cx="23" cy="12" r="4" fill="#fff"/>
    <path d="M23 32c-6 8-20 6-20 20 0 8 10 12 22 12" stroke="#0c4f8c" stroke-width="2.5" fill="none"/>
    <rect x="24" y="50" width="70" height="22" rx="8" fill="#1d8fd0"/>
    <path d="M36 50l8-13h28l8 13z" fill="#1d8fd0"/>
    <circle cx="40" cy="72" r="7" fill="#0c4f8c"/><circle cx="40" cy="72" r="3" fill="#fff"/>
    <circle cx="78" cy="72" r="7" fill="#0c4f8c"/><circle cx="78" cy="72" r="3" fill="#fff"/>
    <path d="M52 24a14 14 0 0 1 16 0M55 29a8 8 0 0 1 10 0" stroke="#0c4f8c" stroke-width="2.2" fill="none"/>
  </g>
  <!-- understanding your needs -->
  <g transform="translate(672 1498)">
    <path d="M14 16l4-12h20l4 12z" fill="#0c4f8c"/>
    <rect x="10" y="14" width="36" height="12" rx="4" fill="#0c4f8c"/>
    <path d="M28 98L4 70a17 17 0 0 1 24-24 17 17 0 0 1 24 24z" fill="#1d8fd0"/>
    <path d="M14 66l14 14 16-18" stroke="#fff" stroke-width="3" fill="none"/>
  </g>
  <!-- proprietary advertising displays -->
  <g transform="translate(862 1522)">
    <path d="M4 40c0-10 6-14 16-16l14-16h30l18 16c10 2 16 6 16 16v8H4z" fill="#0c4f8c"/>
    <path d="M38 12h22l12 12H28z" fill="#fff"/>
    <circle cx="26" cy="48" r="10" fill="#0c4f8c"/><circle cx="26" cy="48" r="5" fill="#fff"/>
    <circle cx="78" cy="48" r="10" fill="#0c4f8c"/><circle cx="78" cy="48" r="5" fill="#fff"/>
    <text x="52" y="40" text-anchor="middle" font-family="Poppins, sans-serif" font-size="20" font-weight="500" fill="#fff">Ad</text>
  </g>
</svg>
<div class="abs service-label" style="left:185px;top:1613px">CUSTOMIZING YOUR CAMPAIGN</div>
<div class="abs service-label" style="left:395px;top:1434px">LAUNCHING AND TRACKING</div>
<div class="abs service-label" style="left:608px;top:1613px">UNDERSTANDING YOUR NEEDS</div>
<div class="abs service-label" style="left:786px;top:1434px;width:250px">PROPRIETARY ADVERTISING DISPLAYS</div>

<!-- call to action -->
<div class="abs cta" role="img" aria-label="Blue-tinted background of a car engine"></div>
<div class="abs display cta-title">WE’RE READY TO HELP!</div>
<div class="abs cta-sub">FEEL FREE TO CONTACT US TODAY</div>
<div class="abs field" style="left:489px">NAME*</div>
<div class="abs field" style="left:741px">EMAIL*</div>
<div class="abs send">SEND</div>

<!-- stats -->
<div class="abs display section-title" style="top:2050px">VORTELANE STATS</div>
<div class="abs stat" style="left:178px;top:2140px"><div class="stat-num">84%</div><div class="stat-label">Customer Retention Rate</div></div>
<div class="abs stat" style="left:616px;top:2140px"><div class="stat-num">150%</div><div class="stat-label">Year-Over-Year Growth</div></div>
<div class="abs divider"></div>

<!-- blog -->
<div class="abs display section-title" style="top:2394px">LATEST BLOG</div>
<article class="abs card" style="left:89px">
  <div class="card-img" role="img" aria-label="Side mirror of a dark car at sunset on an open road" style="background:linear-gradient(120deg,#2a2522,#6d4a35 45%,#e59a4a 70%,#3a2e2a)"></div>
  <div class="card-body">
    <div class="card-date">AUGUST 9, 2020</div>
    <div class="card-title">SOME BLOG HEADING GOES HERE WITH DESCRIPTION...</div>
    <div class="card-text">Quis ipsum suspendisse ultrices Risus viverra maecenas accumsan lacus vel facilisis...</div>
    <span class="card-link">READ MORE</span>
  </div>
</article>
<article class="abs card" style="left:439px">
  <div class="card-img" role="img" aria-label="Child leaning out of a car window" style="background:linear-gradient(120deg,#4a4542,#8a6a52 50%,#c8a27a 75%,#3d3835)"></div>
  <div class="card-body">
    <div class="card-date">AUGUST 9, 2020</div>
    <div class="card-title">SOME BLOG HEADING GOES HERE WITH DESCRIPTION...</div>
    <div class="card-text">Quis ipsum suspendisse ultrices Risus viverra maecenas accumsan lacus vel facilisis...</div>
    <span class="card-link">READ MORE</span>
  </div>
</article>
<article class="abs card" style="left:788px">
  <div class="card-img" role="img" aria-label="Yellow sports car driving on a road" style="background:linear-gradient(160deg,#8a8f88,#c9c62a 45%,#e6dc1f 60%,#4b4e52)"></div>
  <div class="card-body">
    <div class="card-date">AUGUST 9, 2020</div>
    <div class="card-title">SOME BLOG HEADING GOES HERE WITH DESCRIPTION...</div>
    <div class="card-text">Quis ipsum suspendisse ultrices Risus viverra maecenas accumsan lacus vel facilisis...</div>
    <span class="card-link">READ MORE</span>
  </div>
</article>

<!-- partners -->
<div class="abs display section-title" style="top:2967px">OUR PARTNERS</div>
<div class="abs partner" style="left:89px" aria-label="Partner badge"><span></span></div>
<div class="abs partner" style="left:296px" aria-label="Partner badge"><span></span></div>
<div class="abs partner" style="left:502px" aria-label="Partner badge"><span></span></div>
<div class="abs partner" style="left:708px" aria-label="Partner badge"><span></span></div>
<div class="abs partner" style="left:915px" aria-label="Partner badge"><span></span></div>

<!-- footer -->
<div class="abs footer"></div>
<div class="abs footer-logo">VORTELANE</div>
<div class="abs social" style="left:122px" aria-label="Social link"><i></i></div>
<div class="abs social" style="left:168px" aria-label="Social link"><i></i></div>
<div class="abs social" style="left:212px" aria-label="Social link"><i></i></div>

<div class="abs fcol-title" style="left:384px">INFORMATION</div>
<div class="abs fcol" style="left:385px">My account<br>Wishlist<br>Checkout<br>Cart<br>Contact</div>
<div class="abs fcol-title" style="left:558px">QUICK LINKS</div>
<div class="abs fcol" style="left:558px">About<br>Blog<br>Shop<br>Wishlist<br>Contact</div>
<div class="abs fcol-title" style="left:705px">SUPPORT</div>
<div class="abs fcol" style="left:705px">Blog<br>Contact<br>Return Policy<br>Online Support<br>Money Back warrenty</div>
<div class="abs fcol-title" style="left:888px">CONTACT US</div>
<div class="abs fcontact" style="top:3316px">
  <svg width="12" height="12" viewBox="0 0 24 24" style="margin-top:4px"><path d="M6.6 10.8a15 15 0 0 0 6.6 6.6l2.2-2.2c.3-.3.7-.4 1-.2 1.1.4 2.3.6 3.6.6.6 0 1 .4 1 1V20c0 .6-.4 1-1 1A17 17 0 0 1 3 4c0-.6.4-1 1-1h3.5c.6 0 1 .4 1 1 0 1.3.2 2.5.6 3.6.1.3 0 .7-.2 1z" fill="#cfe6f5"/></svg>
  <span>+08 123 456 7890</span></div>
<div class="abs fcontact" style="top:3355px">
  <svg width="12" height="12" viewBox="0 0 24 20" style="margin-top:4px"><rect x="1" y="2" width="22" height="16" rx="2" fill="#cfe6f5"/><path d="M2 4l10 7 10-7" stroke="#2388c9" stroke-width="2" fill="none"/></svg>
  <span>Info@example.com/</span></div>
<div class="abs fcontact" style="top:3393px">
  <svg width="12" height="14" viewBox="0 0 20 24" style="margin-top:3px"><path d="M10 1a8 8 0 0 1 8 8c0 6-8 14-8 14S2 15 2 9a8 8 0 0 1 8-8z" fill="#cfe6f5"/><circle cx="10" cy="9" r="3" fill="#2388c9"/></svg>
  <span>214 Harbor Lane Coral Bay<br>FL 30412/</span></div>

<div class="abs to-top"></div>
<svg class="abs" style="left:1144px;top:3498px" width="12" height="12" viewBox="0 0 12 12"><path d="M2 8l4-4 4 4" stroke="#fff" stroke-width="2" fill="none"/></svg>
<div class="abs footer-rule"></div>
<div class="abs copyright">© Copyright 2020 All Right Reserved</div>
<div class="abs pay" style="left:969px" aria-label="Payment method"></div>
<div class="abs pay" style="left:1018px;background:#dfe9f3" aria-label="Payment method"></div>
<div class="abs pay" style="left:1067px" aria-label="Payment method"></div>

</body>
</html>
```